Design a double sided business card

We are looking for a clean, eye-catching, and contemporary design that enhances the brand and presents a premium, professional image. Our preference is for a brown card with black gloss detailing and embossed elements; however, we are open to creative input and design suggestions that best achieve a strong visual impact.

Please see the attached existing business card for reference. We use both black and brown colours consistently across our branding.

On sample provided

```html
<!DOCTYPE html>
<html lang="en">
<head>
<meta charset="utf-8">
<title>Marlowe – Business Card</title>
<link href="https://fonts.googleapis.com/css2?family=Montserrat:wght@500;600;700&family=Work+Sans:wght@400;500&display=swap" rel="stylesheet">
<style>
  :root {
    --page: #d6d6d4;
    --card: #030303;
    --gold: #b7a68d;
    --gold-soft: #a8977f;
  }
  * { margin: 0; padding: 0; box-sizing: border-box; }
  html, body { width: 1200px; height: 955px; overflow: hidden; }
  body { background: var(--page); position: relative; font-family: "Work Sans", sans-serif; color: var(--gold); }

  .card {
    position: absolute;
    left: 334px;
    width: 551px;
    height: 314px;
    background: var(--card);
    box-shadow: 0 6px 14px rgba(0,0,0,0.35);
  }
  .card--front { top: 141px; }
  .card--back { top: 513px; }

  /* front */
  .brand-mark { position: absolute; left: 43px; top: 44px; width: 48px; height: 45px; border: 3px solid var(--gold); }
  .brand-rule { position: absolute; left: 103px; top: 44px; width: 2px; height: 45px; background: var(--gold); }
  .brand-name {
    position: absolute; left: 115px; top: 53px;
    font-family: "Montserrat", sans-serif; font-weight: 700;
    font-size: 22px; letter-spacing: 3px; line-height: 1;
  }
  .person { position: absolute; left: 127px; top: 160px; }
  .person__name { font-family: "Montserrat", sans-serif; font-weight: 500; font-size: 20px; line-height: 1; }
  .person__role { font-family: "Montserrat", sans-serif; font-weight: 600; font-size: 11.5px; letter-spacing: 0.6px; margin-top: 3px; }
  .contact-rule { position: absolute; left: 250px; top: 146px; width: 2px; height: 68px; background: var(--gold); }
  .contact-list { position: absolute; left: 277px; top: 141px; list-style: none; }
  .contact-list li { display: flex; align-items: center; height: 19.5px; font-size: 12px; letter-spacing: 0.3px; }
  .contact-list svg { width: 11px; height: 11px; margin-right: 16px; flex: none; }
  .address { position: absolute; left: 128px; top: 259px; font-size: 11px; letter-spacing: 0.5px; color: var(--gold-soft); }

  /* back */
  .back-mark { position: absolute; left: 229px; top: 93px; width: 77px; height: 70px; border: 4px solid var(--gold); }
  .back-name {
    position: absolute; left: 0; right: 0; top: 177px; text-align: center;
    font-family: "Montserrat", sans-serif; font-weight: 700;
    font-size: 29px; letter-spacing: 5px; line-height: 1;
  }
  .back-url { position: absolute; left: 0; right: 0; top: 254px; text-align: center; font-size: 16px; letter-spacing: 2.2px; }
</style>
</head>
<body>

<section class="card card--front">
  <div class="brand-mark"></div>
  <div class="brand-rule"></div>
  <div class="brand-name">MARLOWE</div>

  <div class="person">
    <p class="person__name">Dev Arora</p>
    <p class="person__role">Director</p>
  </div>
  <div class="contact-rule"></div>

  <ul class="contact-list">
    <li>
      <svg viewBox="0 0 12 12" aria-hidden="true"><path d="M2.5 1 L4.5 1 L5.2 3.4 L4 4.4 C4.6 6 6 7.4 7.6 8 L8.6 6.8 L11 7.5 L11 9.5 C11 10.3 10.3 11 9.5 11 C5 11 1 7 1 2.5 C1 1.7 1.7 1 2.5 1 Z" fill="var(--gold)"/></svg>
      0800 555 0142
    </li>
    <li>
      <svg viewBox="0 0 12 12" aria-hidden="true"><rect x="3" y="0.7" width="6" height="10.6" rx="1" fill="none" stroke="var(--gold)" stroke-width="1.2"/><circle cx="6" cy="9.5" r="0.6" fill="var(--gold)"/></svg>
      07700900461
    </li>
    <li>
      <svg viewBox="0 0 12 12" aria-hidden="true"><rect x="1" y="2.5" width="10" height="7" fill="var(--gold)"/><path d="M1 2.5 L6 6.5 L11 2.5" fill="none" stroke="var(--card)" stroke-width="1"/></svg>
      dev@marlowe.co.uk
    </li>
    <li>
      <svg viewBox="0 0 12 12" aria-hidden="true"><g fill="none" stroke="var(--gold)" stroke-width="1"><circle cx="6" cy="6" r="5"/><ellipse cx="6" cy="6" rx="2.2" ry="5"/><path d="M1 6 H11 M2 3.5 H10 M2 8.5 H10"/></g></svg>
      marlowe.co.uk
    </li>
  </ul>

  <p class="address">The Yard Elm Court Lane, Northmoor UB0 0AA</p>
</section>

<section class="card card--back">
  <div class="back-mark"></div>
  <div class="back-name">MARLOWE</div>
  <div class="back-url">www.marlowe.co.uk</div>
</section>

</body>
</html>
```